Very Simple Web Redesign Project - Using Photoshop

Required is a very simple website home page redesign for the following site: http://www.tallowcrestslate.com.au/
I require this as a Photoshop design.
The basic look and feel of the site needs to remain.
Specifically the colours don't need to be changed.
The positioning of the site is currently correct for the target market.
The site does not need to be made super slick looking. Just upgraded to a new version.
The current text can all be used.
The only menus necessary are a horizontal menu at the top, and a simple horizontal text menu at the bottom of the page. Do NOT retain the vertical menu on the home page (having the items "Our Gallery", "Our Services", "Enquire Now").
Give the horizontal menu the following items:
Home | Slate Roof Repairs | Slate Reroofing | Slate Roof Benefits | Other Services | Photo Gallery | FAQ's | Free Quote | Contact Us
The picture of the house at the top RHS of the page needs to be reduced in size by approx 50% and moved to the top LHS of the page.
Please place the following text into the top of the page:
"Call Now: 0427 618 392"
Keep the four pictures on the home page layout. Some larger images attached.
Thanks,
Rob
Updates
Hi,
Thanks for all the designs.
I am working with my client to get which one they like the most.
Thanks,
Rob

```html
<!DOCTYPE html>
<html lang="en">
<head>
<meta charset="utf-8">
<title>Tallowcrest Slate – Slate Roof Specialists</title>
<link rel="stylesheet" href="https://fonts.googleapis.com/css2?family=Arimo:wght@400;700&family=Noto+Sans:wght@400;700&family=Lora:wght@500&display=swap">
<style>
  :root {
    --green-top: #4fa50a;
    --green-header: #3e8d1d;
    --green-button: #4a8c22;
    --green-dot: #3b8a1a;
    --green-footer: #3a8707;
    --green-footer-inner: #2a5d12;
    --green-heading: #2f9a16;
    --grey-side: #353735;
    --grey-body: #c5c5d0;
    --grey-panel: #e9e9ee;
    --white-panel: #f5f5f9;
    --logo-blue: #cfe6ff;
    --call-yellow: #ffff00;
    --text-dark: #111111;
    --maroon: #4a0e0e;
    --olive: #6e7a0f;
  }
  * { box-sizing: border-box; margin: 0; padding: 0; }
  html, body { width: 1200px; height: 1113px; overflow: hidden; }
  body { position: relative; background: var(--grey-side); font-family: "Noto Sans", Verdana, sans-serif; color: var(--text-dark); }
  .abs { position: absolute; }

  .top-bar { left: 0; top: 0; width: 1200px; height: 48px; background: var(--green-top); }
  .date { left: 27px; top: 19px; font-family: "Arimo", Arial, sans-serif; font-size: 15px; color: #1d2a10; }
  .call-icon { left: 746px; top: 15px; width: 48px; height: 49px; }
  .call-now { left: 804px; top: 22px; font-family: "Arimo", Arial, sans-serif; font-weight: 700; font-size: 21px; color: var(--call-yellow); }

  .header { left: 0; top: 48px; width: 1200px; height: 183px; background: linear-gradient(180deg, #3f8f1f 0%, #3a8a1c 100%); }
  .brand-mark { left: 78px; top: 105px; width: 56px; height: 56px; background: var(--logo-blue); }
  .brand-name { left: 194px; top: 120px; font-family: "Lora", Georgia, serif; font-weight: 500; font-size: 54px; color: var(--logo-blue); line-height: 1; }

  .nav-band { left: 0; top: 231px; width: 1200px; height: 62px; background: var(--green-top); }
  .nav-line { left: 0; width: 1200px; height: 1px; background: #ffffff; }
  .main-nav { left: 103px; top: 250px; height: 29px; display: flex; list-style: none; font-family: "Arimo", Arial, sans-serif; font-size: 16px; color: #fff; }
  .main-nav li { padding: 0 7px; line-height: 29px; border-left: 1px solid #fff; }
  .main-nav li:first-child { border-left: none; }

  .body-area { left: 46px; top: 293px; width: 1109px; height: 670px; background: var(--grey-body); }

  .side-panel { left: 75px; top: 321px; width: 278px; height: 631px; background: var(--grey-panel); border-radius: 8px; }
  .intro-card { left: 86px; top: 339px; width: 253px; height: 251px; background: var(--white-panel); border-radius: 6px; }
  .quote-box { left: 97px; top: 366px; width: 229px; height: 43px; border: 1px solid var(--green-heading); padding: 1px 15px; font-size: 16px; line-height: 19px; color: var(--maroon); }
  .service-area { left: 97px; top: 428px; width: 238px; font-size: 15.5px; line-height: 19.5px; letter-spacing: 0.2px; }

  .feedback { left: 89px; top: 610px; width: 245px; height: 332px; background: var(--grey-body); border-radius: 6px; }
  .feedback-title { left: 121px; top: 633px; width: 182px; height: 41px; background: var(--green-button); border-radius: 7px; color: #fff; font-size: 21px; text-align: center; line-height: 41px; }
  .field { left: 128px; width: 196px; height: 26px; background: #fff; border: 1px solid var(--green-heading); font-family: "Arimo", Arial, sans-serif; font-size: 14px; padding-left: 13px; line-height: 24px; }
  .enquiry { left: 106px; top: 789px; width: 219px; height: 87px; background: #fff; border: 1px solid var(--green-heading); font-family: "Arimo", Arial, sans-serif; font-size: 14px; padding: 8px 9px; }
  .pref { left: 104px; top: 883px; font-size: 14.5px; }
  .check { top: 906px; width: 14px; height: 14px; background: #fff; border: 1px solid #2a4d14; }
  .check-label { top: 905px; font-size: 11.5px; }
  .submit { left: 229px; top: 930px; width: 76px; height: 16px; background: var(--olive); border-radius: 8px; color: #fff; font-family: "Arimo", Arial, sans-serif; font-weight: 700; font-size: 11px; text-align: center; line-height: 16px; }

  .slide { left: 409px; top: 321px; width: 668px; height: 288px; background: linear-gradient(180deg, #9bb7d9 0%, #7d8a96 40%, #5d6b4a 75%, #d9d9d2 100%); }
  .dot { top: 620px; width: 25px; height: 25px; border-radius: 50%; background: var(--green-dot); }

  .content { left: 368px; top: 650px; width: 766px; height: 297px; background: var(--white-panel); border-radius: 8px; }
  .content-title { left: 388px; top: 666px; width: 399px; font-size: 16.5px; font-weight: 700; color: var(--green-heading); border-bottom: 1px solid var(--green-heading); padding-bottom: 1px; }
  .content-text { left: 389px; top: 702px; width: 730px; font-size: 15px; line-height: 20px; letter-spacing: 0.15px; }
  .content-text p { margin-bottom: 20px; }

  .footer { left: 0; top: 963px; width: 1200px; height: 150px; background: var(--green-footer); }
  .footer-inner { left: 75px; top: 978px; width: 1062px; height: 115px; background: var(--green-footer-inner); border-radius: 7px; }
  .footer-nav { left: 75px; top: 1020px; width: 1062px; text-align: center; font-family: "Arimo", Arial, sans-serif; font-size: 14.5px; color: #d8e8cc; }
  .copyright { left: 75px; top: 1050px; width: 1062px; text-align: center; font-family: "Arimo", Arial, sans-serif; font-weight: 700; font-size: 13.5px; color: #fff; }
</style>
</head>
<body>
  <div class="abs top-bar"></div>
  <div class="abs date">Monday, November 14, 2011 03:41 PM</div>
  <svg class="abs call-icon" viewBox="0 0 48 49" aria-hidden="true">
    <rect x="1" y="1" width="46" height="47" rx="7" fill="#1468b8" stroke="#0b3e70" stroke-width="2"/>
    <path d="M15 9c3-1 5 4 6 7s-2 4-2 6c1 4 5 9 9 10 2 0 3-3 6-2s6 5 3 8c-4 4-10 3-16-3S8 18 11 12c1-1 2-2 4-3z" fill="#fff"/>
  </svg>
  <div class="abs call-now">Call Now: 0427 618 392</div>

  <header class="abs header"></header>
  <div class="abs brand-mark"></div>
  <div class="abs brand-name">Tallowcrest Slate</div>

  <div class="abs nav-band"></div>
  <div class="abs nav-line" style="top:250px"></div>
  <div class="abs nav-line" style="top:279px"></div>
  <ul class="abs main-nav">
    <li>Home</li><li>Slate Roof Repairs</li><li>Slate Reroofing</li><li>Slate Roof Benefits</li><li>Other Services</li><li>Photo Gallery</li><li>FAQ's</li><li>Free Quote</li><li>Contact Us</li>
  </ul>

  <main>
    <div class="abs body-area"></div>

    <aside>
      <div class="abs side-panel"></div>
      <div class="abs intro-card"></div>
      <div class="abs quote-box">Call now and arrange a free quote:</div>
      <p class="abs service-area">We service all inner city sub-urbs of Sydney roughly cover-ing an area encompassing Gordon to Epping, Mosman to Bondi, Coogee to Kogarah and Kingsgrove to Burwood and Concord</p>

      <div class="abs feedback"></div>
      <div class="abs feedback-title">Feed Back</div>
      <div class="abs field" style="top:693px">Name</div>
      <div class="abs field" style="top:723px">Phone</div>
      <div class="abs field" style="top:753px">Email</div>
      <div class="abs enquiry">Enquiry</div>
      <div class="abs pref">Preferred Contact</div>
      <div class="abs check" style="left:137px"></div>
      <div class="abs check-label" style="left:164px">Email</div>
      <div class="abs check" style="left:213px"></div>
      <div class="abs check-label" style="left:233px">Telephone</div>
      <div class="abs submit">Submit</div>
    </aside>

    <div class="abs slide" role="img" aria-label="Photo of a slate roof on a period house framed by trees"></div>
    <div class="abs dot" style="left:637px; border:2px solid #e6f2dc"></div>
    <svg class="abs" style="left:641px; top:624px" width="17" height="17" viewBox="0 0 17 17" aria-hidden="true">
      <circle cx="8.5" cy="8.5" r="7" fill="none" stroke="#fff" stroke-width="1.2"/>
      <path d="M8.5 3.5L12 12L8.5 10L5 12Z" fill="#fff"/>
    </svg>
    <div class="abs dot" style="left:665px"></div>
    <div class="abs dot" style="left:694px"></div>
    <div class="abs dot" style="left:723px"></div>
    <div class="abs dot" style="left:752px"></div>

    <section>
      <div class="abs content"></div>
      <h1 class="abs content-title">Tallowcrest Slate - the Slate Roof Specialists</h1>
      <div class="abs content-text">
        <p>At Tallowcrest Slate we specialize in the upkeep, maintenance, repair and replacement of all types of slate roof as well as wood shingles.&nbsp; We can track down the leak that just won't go away or give your house a complete re-roof. We can also provide all your guttering needs.</p>
        <p>&nbsp;Tallowcrest Slate is a small company and as such we do not have the overheads that larger companies do.&nbsp; Quality work and attention to detail are our trademark.</p>
        <p>&nbsp;All photos on this website consist of work which I have personally done.&nbsp; The above photos provide at a quick glance a reasonable cross section of the type of work I do.</p>
        <p>&nbsp;By clicking on the Photo Gallery link you can see other work including some before and after shots.</p>
      </div>
    </section>
  </main>

  <footer>
    <div class="abs footer"></div>
    <div class="abs footer-inner"></div>
    <nav class="abs footer-nav">Home &nbsp; Slate Roof Repairs | Slate Reroofing | Slate Roof Benefits | Other Services | Photo Gallery | FAQ's | Free Quote | Contact Us</nav>
    <div class="abs copyright">© 2009 Tallowcrest Slate</div>
  </footer>
</body>
</html>
```